Property Developer Business card design

we need a business card design + printing for a new Property developer company based in melbourne.
We are a group of investors investing in a property developer business. We have more projects involved in residential property as opposed to commercial property but we are involved in both market. we also provide consulting services with overseas investors willing to invest in the australian property market.
Updates
I have uploaded the logo. I'm not very convince with the colors of my logo... any suggestion please?.
Thanks guys!
Target Market(s)
property investors or person willing to purchase investment property
Industry/Entity Type
Residential
Contact Information for Business Card
Tallgrove Holdings Australia Pty Ltd
Look and feel
Each slider illustrates characteristics of the customer's brand and the style your logo design should communicate.

```html
<!DOCTYPE html>
<html lang="en">
<head>
<meta charset="utf-8">
<title>Tallgrove Holdings – Business Card Presentation</title>
<link rel="stylesheet" href="https://fonts.googleapis.com/css2?family=Tenor+Sans&display=swap">
<style>
:root{
  --card-centre:#ffffff;
  --card-edge:#c8c8c8;
  --ink:#111111;
  --ink-soft:#2a2a2a;
  --label-teal:#0d4a44;
  --card-shadow:rgba(0,0,0,.45);
}
*{margin:0;padding:0;box-sizing:border-box}
html,body{width:1200px;height:1200px;overflow:hidden}
body{position:relative;font-family:"Tenor Sans",sans-serif;color:var(--ink)}
.backdrop{position:absolute;inset:0;width:1200px;height:1200px}
.card{
  position:absolute;left:30px;width:666px;height:384px;overflow:hidden;
  background:radial-gradient(ellipse at 50% 45%,var(--card-centre) 0%,#ececec 45%,var(--card-edge) 100%);
  box-shadow:2px 4px 8px var(--card-shadow);
}
.card--front{top:-6px}
.card--back-one{top:402px}
.card--back-two{top:816px}
.view-label{
  position:absolute;font-size:56px;color:var(--label-teal);line-height:1;white-space:nowrap;
}
.view-label--front{left:734px;top:104px}
.view-label--one{left:704px;top:502px}
.view-label--two{left:704px;top:900px}
.brand{position:absolute;text-align:center;white-space:nowrap}
.brand__name{letter-spacing:1px;color:var(--ink)}
.brand__sub{font-variant:small-caps;letter-spacing:1.5px;color:var(--ink-soft)}
.card--front .brand{left:0;width:666px;top:144px}
.card--front .brand__name{font-size:32px}
.card--front .brand__sub{font-size:20px;margin-top:20px}
.card--back-one .brand{left:30px;width:270px;top:164px}
.card--back-one .brand__name{font-size:16px;letter-spacing:.5px}
.card--back-one .brand__sub{font-size:12px;margin-top:14px}
.card--back-two .brand{left:198px;width:300px;top:160px}
.card--back-two .brand__name{font-size:17px;letter-spacing:.5px}
.card--back-two .brand__sub{font-size:12px;margin-top:14px}
.divider{position:absolute;left:314px;top:48px;width:1px;height:282px;background:var(--ink)}
.holder{position:absolute;white-space:nowrap}
.holder__name{font-size:22px;letter-spacing:1.5px}
.holder__role{font-size:11px;letter-spacing:1.5px;margin-top:6px}
.card--back-one .holder{left:322px;top:50px}
.card--back-two .holder{left:472px;top:46px}
.contacts{position:absolute;color:var(--ink-soft);white-space:nowrap}
.contacts dt{display:inline;color:var(--ink)}
.contacts dd{display:inline}
.card--back-one .contacts{left:324px;top:216px;font-size:13px}
.card--back-one .contacts div{margin-bottom:14px}
.card--back-two .contacts{left:64px;top:324px;font-size:12px;display:grid;grid-template-columns:232px 178px auto;row-gap:9px}
.contacts__wide{grid-column:span 2}
</style>
</head>
<body>
<svg class="backdrop" role="img" aria-label="Ornamental damask pattern backdrop in beige and cream" viewBox="0 0 1200 1200">
  <defs>
    <radialGradient id="backdropTone" cx="60%" cy="45%" r="75%">
      <stop offset="0" stop-color="#f3eee3"/>
      <stop offset="1" stop-color="#d6ccb6"/>
    </radialGradient>
  </defs>
  <rect width="1200" height="1200" fill="url(#backdropTone)"/>
</svg>

<section class="card card--front">
  <div class="brand">
    <div class="brand__name">TALLGROVE HOLDINGS</div>
    <div class="brand__sub">Australia Pty Ltd</div>
  </div>
</section>
<p class="view-label view-label--front">front</p>

<section class="card card--back-one">
  <div class="brand">
    <div class="brand__name">TALLGROVE HOLDINGS</div>
    <div class="brand__sub">Australia Pty Ltd</div>
  </div>
  <div class="divider"></div>
  <div class="holder">
    <div class="holder__name">DANIEL HART</div>
    <div class="holder__role">MANAGER</div>
  </div>
  <dl class="contacts">
    <div><dt>Phone:</dt> <dd>+61439027458</dd></div>
    <div><dt>Email:</dt> <dd>daniel@tallgroveholdings.com</dd></div>
    <div><dt>Web:</dt> <dd>www.tallgroveholdings.com</dd></div>
    <div><dt>Address:</dt> <dd>14 Corrin St, Richmond, VIC, 3121</dd></div>
  </dl>
</section>
<p class="view-label view-label--one">back option one</p>

<section class="card card--back-two">
  <div class="holder">
    <div class="holder__name">DANIEL HART</div>
    <div class="holder__role">MANAGER</div>
  </div>
  <div class="brand">
    <div class="brand__name">TALLGROVE HOLDINGS</div>
    <div class="brand__sub">Australia Pty Ltd</div>
  </div>
  <dl class="contacts">
    <div><dt>Email:</dt> <dd>daniel@tallgroveholdings.com</dd></div>
    <div><dt>Phone:</dt> <dd>+61439027458</dd></div>
    <div><dt>Fax:</dt> <dd>800.412.7390</dd></div>
    <div><dt>Web:</dt> <dd>www.tallgroveholdings.com</dd></div>
    <div class="contacts__wide"><dt>Address:</dt> <dd>14 Corrin St, Richmond, VIC, 3121</dd></div>
  </dl>
</section>
<p class="view-label view-label--two">back option two</p>
</body>
</html>
```